Travel Company is looking for a STAND OUT Business Card

I need a unique Business Card that will truly stand out. Nothing too busy. Simple is good, right? Not looking for a standard design either. No cookie cutter layout. We are a Travel Company that works more with Companies than Travelers. I had an idea to focus and emphasis on the 2 logo a bit more. This is not necessary, however thought it would look interesting. I am just looking for something interesting and a bit different. Does't have to completely off the wall crazy, just not your run of the mill business card.

Target Market(s)

Hoteliers, Resort Management, Call Centers, Executives, Travelers, Families, Businesses

Industry/Entity Type

Hospitality

Contact Information for Business Card

President/CEO - Marcus T Bellamy (title not necessary if design doesn't allow for it)
contact - (407) 555-0186
email - mbellamy@wayfarenow.example
address - 4812 Quillmore Ave #164
Orlando, FL 32804
website - www.wayfarenow.example

Font styles to use
Serif
Other font styles liked:
• Avenir Next LT Pro BOLD

Requirements
Must have
• simple look and design. Unique design
Nice to have
• I attached the 2 logo separate from the main logo. This can be used separately from the Main Logo, together with the main logo or as main logo. I included the logo font. Use it or not, designers choice.
Should not have
• cookie cutter design. Little use of red other than the logo

```html
<!DOCTYPE html>
<html lang="en">
<head>
<meta charset="utf-8">
<title>Wayfare Now — Business Card</title>
<link rel="stylesheet" href="https://fonts.googleapis.com/css2?family=Open+Sans:wght@400;600;700;800&display=swap">
<style>
  :root {
    --backdrop: #3b3b3b;
    --card: #252525;
    --white: #ffffff;
    --red: #e41e26;
    --muted: #8a8a8a;
  }
  * { box-sizing: border-box; margin: 0; padding: 0; }
  html, body {
    width: 1200px;
    height: 1000px;
    overflow: hidden;
    background: var(--backdrop);
    font-family: "Open Sans", Arial, sans-serif;
  }
  .canvas { position: relative; width: 1200px; height: 1000px; }
  .card {
    position: absolute;
    left: 288px;
    width: 625px;
    height: 357px;
    background: var(--card);
    overflow: hidden;
    box-shadow: 0 6px 16px rgba(0,0,0,0.35);
  }
  .card--front { top: 140px; }
  .card--back { top: 532px; }

  .brand {
    position: absolute;
    display: flex;
    align-items: center;
    gap: 14px;
    color: var(--white);
    font-weight: 800;
    letter-spacing: -1px;
    line-height: 1;
  }
  .brand__dot {
    border-radius: 50%;
    background: var(--red);
    flex: none;
  }
  .card--front .brand {
    left: 50%;
    top: 50%;
    transform: translate(-50%, -60%);
    font-size: 62px;
  }
  .card--front .brand__dot { width: 30px; height: 30px; }

  .card--back .brand {
    right: 38px;
    top: 150px;
    font-size: 34px;
    gap: 10px;
  }
  .card--back .brand__dot { width: 18px; height: 18px; }

  .holder {
    position: absolute;
    left: 0;
    top: 55px;
    padding-left: 34px;
    border-left: 6px solid var(--red);
  }
  .holder__name {
    color: var(--red);
    font-weight: 700;
    font-size: 16px;
    line-height: 18px;
  }
  .holder__title {
    color: var(--muted);
    font-size: 12.5px;
    line-height: 16px;
  }
  .holder { padding-left: 28px; }

  .contact {
    position: absolute;
    left: 34px;
    top: 216px;
    list-style: none;
    color: var(--muted);
    font-size: 12.5px;
    line-height: 17px;
  }
  .contact__item {
    display: flex;
    align-items: flex-start;
    gap: 7px;
    margin-bottom: 3px;
  }
  .contact__item--address { margin-bottom: 11px; }
  .contact__icon {
    width: 11px;
    height: 11px;
    margin-top: 3px;
    flex: none;
    fill: var(--red);
  }
</style>
</head>
<body>
<main class="canvas">

  <section class="card card--front" aria-label="Card front">
    <div class="brand">
      <span class="brand__name">wayfare now</span>
      <span class="brand__dot" aria-hidden="true"></span>
    </div>
  </section>

  <section class="card card--back" aria-label="Card back">
    <div class="holder">
      <p class="holder__name">Marcus T Bellamy</p>
      <p class="holder__title">President/CEO</p>
    </div>

    <ul class="contact">
      <li class="contact__item contact__item--address">
        <svg class="contact__icon" viewBox="0 0 12 12" aria-hidden="true"><path d="M6 0a4 4 0 0 0-4 4c0 3 4 8 4 8s4-5 4-8a4 4 0 0 0-4-4zm0 5.6A1.6 1.6 0 1 1 6 2.4a1.6 1.6 0 0 1 0 3.2z"/></svg>
        <span>4812 Quillmore Ave #164<br>Orlando, FL 32804</span>
      </li>
      <li class="contact__item">
        <svg class="contact__icon" viewBox="0 0 12 12" aria-hidden="true"><path d="M2.4 0.6l2 2.1-1 1.4c.7 1.6 1.9 2.8 3.5 3.5l1.4-1 2.1 2-1.2 2C5 10.2 1.8 7 .4 1.8z"/></svg>
        <span>(407) 555-0186</span>
      </li>
      <li class="contact__item">
        <svg class="contact__icon" viewBox="0 0 12 12" aria-hidden="true"><path d="M0 2h12v8H0z M0 2l6 4.5L12 2" stroke="#252525" stroke-width="0.9"/></svg>
        <span>mbellamy@wayfarenow.example</span>
      </li>
      <li class="contact__item">
        <svg class="contact__icon" viewBox="0 0 12 12" aria-hidden="true"><circle cx="6" cy="6" r="5.5"/><path d="M.5 6h11M6 .5c-2.5 3-2.5 8 0 11M6 .5c2.5 3 2.5 8 0 11" stroke="#252525" stroke-width="0.8" fill="none"/></svg>
        <span>www.wayfarenow.example</span>
      </li>
    </ul>

    <div class="brand">
      <span class="brand__name">wayfare now</span>
      <span class="brand__dot" aria-hidden="true"></span>
    </div>
  </section>

</main>
</body>
</html>
```